Electrician's Business needs web site for customers to get professional impression of business.

Have a logo, need a web page for customers to visit. Web page should make it easy for customers to approach /contact me, if possible a way for customers to leave their details so I can call them back.
A description/ list of services and advertise how my service is different and better than other electricians.
A gallery to upload photos to, to show completed works from past projects.
Updates

Target Market(s)

Domestic/residential home owner/renter/builder

Industry/Entity Type

Electrician

Coding

Coded - Design and coding required

Number of Pages Required

2 page

Font styles to use
Sans Serif

Colors
0255a3
ffffff

Requirements
Must have
• Appeal to home owner/renter, domestic market.
• Capture contact details of customer & advertise my contact details.
• List of services
Nice to have
• A photo gallery, so I can upload pictures of completed work.
Should not have
• Industrial/construction images.

```html
<!DOCTYPE html>
<html lang="en">
<head>
<meta charset="utf-8">
<title>Volt Harbor – Electrical Services</title>
<link rel="stylesheet" href="https://fonts.googleapis.com/css2?family=Open+Sans:wght@400;600;800&family=Roboto:wght@400;500;700&family=Montserrat:wght@500;700&display=swap">
<style>
:root{
  --brand:#0255a3;
  --brand-mid:#1f6fc4;
  --brand-light:#4aa8ec;
  --sky:#5bbcf5;
  --hero-a:#4a63c9;
  --hero-b:#7d95e3;
  --orange:#f08a1f;
  --orange-light:#f7a94a;
  --white:#ffffff;
  --ink:#222222;
  --muted:#666666;
}
*{box-sizing:border-box;margin:0;padding:0}
html,body{width:1200px;height:2521px;overflow:hidden;background:var(--white)}
body{font-family:"Roboto",sans-serif;color:var(--ink);position:relative}
.page{position:relative;width:1200px;height:2521px;overflow:hidden}
.abs{position:absolute}

/* hero */
.hero{left:0;top:0;width:1200px;height:546px;background:linear-gradient(120deg,var(--hero-a) 0%,#5673d4 55%,var(--hero-b) 100%);overflow:hidden}
.hero-sheen{left:480px;top:0;width:900px;height:546px;background:rgba(255,255,255,.07);transform:skewX(-28deg);transform-origin:top left}
.topbar{left:0;top:0;width:1200px;height:67px;border-bottom:1px solid rgba(255,255,255,.25)}
.brand{left:52px;top:14px;line-height:38px;font-family:"Roboto",sans-serif;font-weight:700;font-size:30px;color:var(--white);display:flex;align-items:center;gap:10px}
.brand-dot{width:14px;height:14px;border-radius:50%;background:var(--white)}
.nav{left:545px;top:0;height:67px;display:flex;align-items:center}
.nav a{font-family:"Roboto",sans-serif;font-size:15px;color:var(--white);text-decoration:none;font-weight:500;margin-right:36px}
.nav .nav-cta{border:2px solid var(--white);border-radius:22px;padding:9px 18px;margin-right:0;margin-left:-4px}
.hero-kicker{left:76px;top:192px;line-height:36px;font-family:"Open Sans",sans-serif;font-size:29px;color:var(--white);display:flex;align-items:center;gap:14px}
.hero-kicker i{display:block;width:46px;height:10px;background:repeating-linear-gradient(135deg,rgba(255,255,255,.85) 0 3px,transparent 3px 6px)}
.hero-title{left:22px;top:221px;line-height:80px;font-family:"Open Sans",sans-serif;font-weight:800;font-size:76px;letter-spacing:1px;color:var(--white);text-shadow:0 4px 8px rgba(0,0,0,.25)}
.hero-call{left:74px;top:307px;line-height:34px;font-family:"Open Sans",sans-serif;font-size:27px;color:var(--white)}
.hero-art{left:857px;top:84px;width:270px;height:312px;border-radius:50%;background:radial-gradient(circle at 50% 42%,rgba(247,211,62,.55),rgba(247,211,62,.12) 60%,transparent 72%)}

/* intro cards */
.card{top:432px;height:195px;border-radius:4px;background:linear-gradient(135deg,var(--brand-mid),var(--brand-light));box-shadow:0 4px 12px rgba(0,0,0,.15);color:var(--white)}
.card h2{font-size:19px;line-height:24px;font-weight:700;text-align:center;margin-top:18px}
.welcome{left:52px;width:535px}
.welcome p{font-size:12.5px;line-height:19px;text-align:center;margin:14px 16px 0}
.quickmail{left:610px;width:535px}
.field{position:absolute;background:var(--white);border-radius:2px;font-size:12px;color:#aaa;padding:8px 10px;height:32px}
.btn-orange{position:absolute;background:var(--orange);color:var(--white);font-size:13px;font-weight:700;text-align:center;border-radius:2px}

/* section heads */
.sec-title{left:0;width:1200px;text-align:center;font-size:23px;line-height:30px;font-weight:700;color:var(--ink)}
.sec-title span{color:var(--brand)}
.dots{left:52px;width:1096px;border-top:2px dotted #555}

/* services */
.svc{width:252px}
.svc-img{position:absolute;left:0;top:22px;width:252px;height:121px;border-radius:2px}
.svc-icon{position:absolute;left:105px;top:0;width:42px;height:42px;border-radius:50%;background:var(--brand-mid);border:2px solid var(--white);display:flex;align-items:center;justify-content:center}
.svc-label{position:absolute;left:11px;top:131px;width:230px;height:57px;border-radius:4px;background:linear-gradient(135deg,var(--brand-mid),var(--brand-light));color:var(--white);font-size:19px;font-weight:700;display:flex;align-items:center;justify-content:center;box-shadow:0 3px 6px rgba(0,0,0,.2)}

/* reasons */
.reasons{left:0;top:1156px;width:1200px;height:296px;background:linear-gradient(135deg,var(--brand-mid) 0%,#2c86d6 50%,var(--brand-light) 100%)}
.reasons .sec-title{color:var(--white);top:35px}
.reasons .dots{top:76px;border-color:rgba(255,255,255,.7)}
.reason{top:108px;width:120px;text-align:center;color:var(--white);font-size:13px;line-height:18px}
.reason-badge{width:67px;height:67px;margin:0 auto 10px;border-radius:50%;background:radial-gradient(circle at 40% 35%,var(--orange-light),var(--orange));display:flex;align-items:center;justify-content:center;box-shadow:0 2px 4px rgba(0,0,0,.2)}

/* work */
.work{width:252px;text-align:center}
.work-img{width:252px;height:207px}
.work h3{font-size:18px;line-height:24px;font-weight:700;margin-top:30px}
.work p{font-family:"Open Sans",sans-serif;font-size:12.5px;line-height:20px;color:var(--muted);margin-top:12px}

/* cta */
.cta{left:55px;top:1955px;width:1068px;height:124px;background:linear-gradient(90deg,var(--brand-mid),var(--sky))}
.cta-art{left:76px;top:1916px;width:134px;height:163px;background:linear-gradient(180deg,rgba(255,255,255,.35),rgba(255,255,255,.12))}
.cta-bar{left:224px;top:2003px;width:2px;height:22px;background:var(--orange)}
.cta-small{left:244px;top:1994px;line-height:16px;font-family:"Montserrat",sans-serif;font-size:12px;font-weight:500;color:var(--white)}
.cta-big{left:244px;top:2014px;line-height:26px;font-family:"Montserrat",sans-serif;font-size:20px;font-weight:700;color:var(--white)}
.cta-btn{left:931px;top:1995px;width:158px;height:44px;border:2px solid var(--white);color:var(--white);font-family:"Montserrat",sans-serif;font-size:12px;font-weight:700;display:flex;align-items:center;justify-content:center}

/* footer */
.footer{left:0;top:2079px;width:1200px;height:442px;background:linear-gradient(135deg,#1a64b8 0%,#2f8cdb 55%,var(--brand-light) 100%);color:var(--white)}
.fcol{top:52px;width:252px}
.fcol h4{font-size:18px;line-height:24px;font-weight:700;margin-bottom:20px}
.fcol p{font-size:12.5px;line-height:19px}
.fcol p+p{margin-top:14px}
.fcol b{font-weight:700}
.socials{display:flex;gap:12px;margin-top:14px}
.socials i{display:block;width:13px;height:13px;border-radius:50%;background:var(--white)}
.ffield{background:var(--white);border-radius:2px;height:32px;margin-bottom:20px;color:#999;font-size:12px;padding:8px 12px}
.ffield.area{height:56px}
.fmap{width:252px;height:212px;background:linear-gradient(135deg,#e8e4da,#d8dde2 60%,#f3c98a)}
.foot-line{left:52px;top:375px;width:1096px;border-top:1px solid rgba(255,255,255,.6)}
.foot-copy{left:52px;top:403px;line-height:18px;font-size:13px;font-weight:700}
.foot-brand{left:0;width:1200px;top:395px;line-height:34px;text-align:center;font-size:28px;font-weight:700}
.foot-rights{right:52px;top:403px;line-height:18px;font-size:13px;font-weight:700}
</style>
</head>
<body>
<div class="page">

  <header class="hero abs">
    <div class="hero-sheen abs"></div>
    <div class="topbar abs"></div>
    <div class="brand abs"><span>Volt Harbor</span><span class="brand-dot"></span></div>
    <nav class="nav abs">
      <a href="#">HOME</a><a href="#">ABOUT</a><a href="#">SERVICES</a><a href="#">OUR WORK</a><a href="#">BLOG</a><a href="#" class="nav-cta">CONTACT US</a>
    </nav>
    <div class="hero-kicker abs"><i></i>DO YOU NEED A NEW<i></i></div>
    <h1 class="hero-title abs">ELECTRICIAN?</h1>
    <p class="hero-call abs">Call Volt Harbor at (555) 014 2290</p>
    <div class="hero-art abs" role="img" aria-label="Glowing yellow light bulb illustration"></div>
  </header>

  <section class="card welcome abs">
    <h2>Welcome We're Volt Harbor</h2>
    <p>Volt Harbor Electric's mission is to provide residential and commercial electrical service above and beyond what is expected. We treat each and every customer as if they were a part of the family. In doing so, Volt Harbor Electric places an emphasis on communicating at every step of the service process. From initial service call, to project completion, we want our customers to know their job is always a priority. Honesty, integrity, and courteous service is what we promise you.</p>
  </section>

  <section class="card quickmail abs">
    <h2>Feel Free to Mail</h2>
    <div class="field" style="left:10px;top:60px;width:114px">Name *</div>
    <div class="field" style="left:144px;top:60px;width:114px">Email *</div>
    <div class="field" style="left:277px;top:60px;width:114px">Subject *</div>
    <div class="field" style="left:411px;top:60px;width:114px">City *</div>
    <div class="field" style="left:10px;top:112px;width:391px;height:45px">Write Your Message Here...</div>
    <div class="btn-orange" style="left:411px;top:119px;width:114px;height:32px;line-height:32px">SEND NOW</div>
  </section>

  <h2 class="sec-title abs" style="top:634px">Our <span>Services</span></h2>
  <div class="dots abs" style="top:674px"></div>

  <div class="svc abs" style="left:52px;top:706px">
    <div class="svc-img" role="img" aria-label="Garden with outdoor lighting at dusk" style="background:linear-gradient(180deg,#3b5a2e,#6f8f3c 60%,#9aa36a)"></div>
    <div class="svc-icon"><svg width="20" height="20" viewBox="0 0 20 20"><circle cx="10" cy="8" r="5" fill="none" stroke="#fff" stroke-width="2"/><rect x="8" y="13" width="4" height="4" fill="#fff"/></svg></div>
    <div class="svc-label">Outdoor Projects</div>
  </div>
  <div class="svc abs" style="left:329px;top:706px">
    <div class="svc-img" role="img" aria-label="Home standby generator beside a house" style="background:linear-gradient(180deg,#6f7d6a,#c9cdc8 55%,#5d7a3e)"></div>
    <div class="svc-icon"><svg width="20" height="20" viewBox="0 0 20 20"><rect x="3" y="6" width="14" height="10" rx="2" fill="#fff"/><rect x="7" y="3" width="6" height="3" fill="#fff"/></svg></div>
    <div class="svc-label">Generators</div>
  </div>
  <div class="svc abs" style="left:607px;top:706px">
    <div class="svc-img" role="img" aria-label="Modern house lit up at night" style="background:linear-gradient(180deg,#1d3560,#34507d 55%,#d19a45)"></div>
    <div class="svc-icon"><svg width="20" height="20" viewBox="0 0 20 20"><circle cx="10" cy="8" r="5" fill="#fff"/><rect x="8" y="13" width="4" height="4" fill="#fff"/></svg></div>
    <div class="svc-label">Lighting</div>
  </div>
  <div class="svc abs" style="left:884px;top:706px">
    <div class="svc-img" role="img" aria-label="Electrician working on a wiring panel" style="background:linear-gradient(135deg,#7aa1c4,#c8d6e2 50%,#4d6f95)"></div>
    <div class="svc-icon"><svg width="20" height="20" viewBox="0 0 20 20"><rect x="6" y="3" width="8" height="14" rx="1" fill="none" stroke="#fff" stroke-width="2"/><rect x="8" y="6" width="4" height="4" fill="#fff"/></svg></div>
    <div class="svc-label">HVAC</div>
  </div>

  <div class="svc abs" style="left:52px;top:948px">
    <div class="svc-img" role="img" aria-label="Electrician fitting a ceiling light" style="background:linear-gradient(180deg,#9ea3a8,#dcdfe2 60%,#c9c34a)"></div>
    <div class="svc-icon"><svg width="20" height="20" viewBox="0 0 20 20"><rect x="3" y="6" width="10" height="6" rx="1" fill="#fff"/><rect x="13" y="8" width="4" height="2" fill="#fff"/><rect x="6" y="12" width="3" height="5" fill="#fff"/></svg></div>
    <div class="svc-label">Renovation</div>
  </div>
  <div class="svc abs" style="left:329px;top:948px">
    <div class="svc-img" role="img" aria-label="Remodelled kitchen with warm lighting" style="background:linear-gradient(180deg,#4a2e1c,#a5723e 55%,#d9b37a)"></div>
    <div class="svc-icon"><svg width="20" height="20" viewBox="0 0 20 20"><path d="M5 4h7l3 3v9H5z" fill="none" stroke="#fff" stroke-width="2"/></svg></div>
    <div class="svc-label">Remodeling</div>
  </div>
  <div class="svc abs" style="left:607px;top:948px">
    <div class="svc-img" role="img" aria-label="Hands holding a tablet with home control app" style="background:linear-gradient(180deg,#6d8cae,#2d3c55 50%,#8f5a3f)"></div>
    <div class="svc-icon"><svg width="20" height="20" viewBox="0 0 20 20"><rect x="3" y="3" width="6" height="6" fill="#fff"/><rect x="11" y="3" width="6" height="6" fill="none" stroke="#fff" stroke-width="2"/><rect x="3" y="11" width="6" height="6" fill="none" stroke="#fff" stroke-width="2"/><rect x="11" y="11" width="6" height="6" fill="#fff"/></svg></div>
    <div class="svc-label">Miscellaneous</div>
  </div>
  <div class="svc abs" style="left:884px;top:948px">
    <div class="svc-img" role="img" aria-label="Chalkboard with drawn question marks and a bulb" style="background:linear-gradient(135deg,#2d2f30,#4a4d4f 70%,#b7b53a)"></div>
    <div class="svc-icon"><svg width="20" height="20" viewBox="0 0 20 20"><rect x="5" y="3" width="10" height="14" rx="2" fill="none" stroke="#fff" stroke-width="2"/><circle cx="10" cy="14" r="1.3" fill="#fff"/></svg></div>
    <div class="svc-label">Request Service</div>
  </div>

  <section class="reasons abs">
    <h2 class="sec-title abs">Great reasons to use Volt Harbor</h2>
    <div class="dots abs"></div>
    <div class="reason abs" style="left:73px"><div class="reason-badge"><svg width="30" height="30" viewBox="0 0 30 30"><path d="M7 15l6 6 10-12" fill="none" stroke="#fff" stroke-width="4"/></svg></div>Insured<br>Electricians</div>
    <div class="reason abs" style="left:207px"><div class="reason-badge"><svg width="30" height="30" viewBox="0 0 30 30"><path d="M4 15L15 5l11 10h-3v10H7V15z" fill="#fff"/><rect x="13" y="18" width="4" height="7" fill="#f08a1f"/></svg></div>Free In-Home<br>Quotes</div>
    <div class="reason abs" style="left:342px"><div class="reason-badge"><svg width="30" height="30" viewBox="0 0 30 30"><circle cx="15" cy="12" r="7" fill="#fff"/><path d="M10 18l-2 9 7-4 7 4-2-9" fill="#fff"/></svg></div>Licensed<br>Experts</div>
    <div class="reason abs" style="left:476px"><div class="reason-badge"><svg width="30" height="30" viewBox="0 0 30 30"><rect x="8" y="4" width="4" height="22" rx="2" fill="#fff"/><rect x="18" y="4" width="4" height="22" rx="2" fill="#fff"/></svg></div>Workmanship &amp;<br>Parts<br>Guaranteed</div>
    <div class="reason abs" style="left:609px"><div class="reason-badge"><span style="font-size:34px;font-weight:700;color:#fff">$</span></div>Upfront, Flat<br>Rate Pricing</div>
    <div class="reason abs" style="left:743px"><div class="reason-badge"><svg width="30" height="30" viewBox="0 0 30 30"><circle cx="15" cy="9" r="5" fill="#fff"/><path d="M6 26c0-7 4-10 9-10s9 3 9 10z" fill="#fff"/></svg></div>Courteous,<br>Uniformed<br>Professionals</div>
    <div class="reason abs" style="left:878px"><div class="reason-badge"><svg width="30" height="30" viewBox="0 0 30 30"><rect x="5" y="7" width="20" height="18" fill="none" stroke="#fff" stroke-width="2"/><path d="M5 12h20M11 12v13M17 12v13M5 18h20" stroke="#fff" stroke-width="1.5"/></svg></div>Scheduled<br>Appointment<br>Times</div>
    <div class="reason abs" style="left:1012px"><div class="reason-badge"><svg width="30" height="30" viewBox="0 0 30 30"><path d="M5 16L16 5h8v8L13 24z" fill="#fff"/><circle cx="20" cy="9" r="2" fill="#f08a1f"/></svg></div>Special Offers</div>
  </section>

  <h2 class="sec-title abs" style="top:1466px">Our <span>Work</span></h2>
  <div class="dots abs" style="top:1508px"></div>

  <article class="work abs" style="left:52px;top:1563px">
    <div class="work-img" role="img" aria-label="Multimeter probes testing colourful wiring" style="background:linear-gradient(135deg,#d9dee4,#3a78c4 55%,#d8c23a)"></div>
    <h3>Ultra Responsive</h3>
    <p>Lorem ipsum dolor sit amet einem,<br>consectetur adipiscing elit, sed do in.</p>
  </article>
  <article class="work abs" style="left:333px;top:1563px">
    <div class="work-img" role="img" aria-label="Row of electrical switchgear cabinets" style="background:linear-gradient(180deg,#e6e8ee,#b9bdc9 60%,#8fd6e2)"></div>
    <h3>Unique Features</h3>
    <p>Eiusmod tempor incididunt ut labore et<br>dolore magna aliqua ut enim ad.</p>
  </article>
  <article class="work abs" style="left:615px;top:1563px">
    <div class="work-img" role="img" aria-label="Room under renovation with exposed ceiling" style="background:linear-gradient(180deg,#3b2a1e,#8a6a4a 50%,#e6c28f)"></div>
    <h3>Easy to Customize</h3>
    <p>Aliquip ex ea commodo consequat. Duis<br>aute irure dolor in reprehenderit.</p>
  </article>
  <article class="work abs" style="left:896px;top:1563px">
    <div class="work-img" role="img" aria-label="Technician checking an electrical panel" style="background:linear-gradient(135deg,#3f4450,#6b7280 55%,#c96a2a)"></div>
    <h3>Layout Builder</h3>
    <p>Duis aute irure dolor in reprehenderit in<br>voluptate velit esse cillum dolore.</p>
  </article>

  <div class="cta abs"></div>
  <div class="cta-art abs" role="img" aria-label="Photo of a friendly electrician"></div>
  <div class="cta-bar abs"></div>
  <p class="cta-small abs">Have Any Questions !</p>
  <p class="cta-big abs">DON'T HESITATE TO CONTACT US ANY TIME.</p>
  <a class="cta-btn abs">CONTACT US</a>

  <footer class="footer abs">
    <div class="fcol abs" style="left:52px">
      <h4>Contact Us</h4>
      <p>Maecenas etos sit amet, consectetur adipiscing elit. Terminal volutpat rutrum metro amet sollicitudin interdum.</p>
      <p><b>Phone:</b> +1 (800) 555 0142</p>
      <p><b>Office:</b> 418 Linden Avenue, Springfield</p>
      <p><b>Email:</b> hello@voltharbor.example</p>
      <div class="socials"><i></i><i></i><i></i><i></i><i></i></div>
    </div>
    <div class="fcol abs" style="left:333px">
      <h4>Feel Free to Mail</h4>
      <div class="ffield">Name *</div>
      <div class="ffield">Email *</div>
      <div class="ffield area">Write Your Message Here...</div>
      <div class="btn-orange" style="position:relative;width:136px;height:32px;line-height:32px">SEND MESSAGE</div>
    </div>
    <div class="fcol abs" style="left:615px">
      <h4>Headquarters</h4>
      <div class="fmap" role="img" aria-label="Street map showing the office location"></div>
    </div>
    <div class="fcol abs" style="left:896px">
      <h4>About Team</h4>
      <p>Enim congue blandit. Lorem ipsum dolor sit amet, consectetur adipiscing elit. Quisque consectetur interdum finibus. Vestibulum ante ipsum primis in faucibus orci. luctus et ultrices posuere.</p>
      <p>Cubilia cras blandit finibus ipsum, id porttitor arcu volutpat a. Integer iaculis erat nec justo malesuada faucibus vel tempus sapien. Vivamus aliquam euismod tristique.</p>
    </div>
    <div class="foot-line abs"></div>
    <p class="foot-copy abs">Copyright 2020</p>
    <p class="foot-brand abs">Volt Harbor</p>
    <p class="foot-rights abs">All Rights Reserved by Volt Harbor</p>
  </footer>

</div>
</body>
</html>
```